Tallow & Mersey Needs New Stationery / Letterhead Design

We need new stationery to match our new logo (attached). Tallow & Mersey is a 34 year old nationwide law firm located in Houston Tx. They do personal injury law and pharmaceutical litigation.

WE DO NOT NEED BUSINESS CARDS.

Attached are several different file formats of the new logo.

Reason: We will make a decision in the next couple days. Finalizing edits now. Thank you!

Target Market(s)

consumers who have been injured due to the negligence of another or by a pharmaceutical drug or defective medical device. Also co-counsel and opposing counsel (law firms0.

Industry/Entity Type

Law Firm

Requirements
Must have
• logo
• Tallow & Mersey, LLP
• 7183 Corvid Lane, Suite 1000
• Brenford, TX 75591
• Tel: (555) 408-1936
• Fax: (555) 408-2275
• www.tallowandmersey.example
• Must have colors in the logo.
• Make the font go with the logo - not necessarily the same, but something that goes well with it.

```html
<!DOCTYPE html>
<html lang="en">
<head>
<meta charset="utf-8">
<title>Tallow &amp; Mersey — Stationery</title>
<link href="https://fonts.googleapis.com/css2?family=Cinzel:wght@500&family=Raleway:wght@400;500&display=swap" rel="stylesheet">
<style>
  :root {
    --backdrop: #aab5b9;
    --navy: #1d2f96;
    --navy-deep: #14226f;
    --paper: #ffffff;
    --paper-shade: #eceef0;
    --ink: #2a2a2e;
    --faint: #d7dbea;
    --serif: "Cinzel", "Times New Roman", serif;
    --sans: "Raleway", Arial, sans-serif;
  }
  * { box-sizing: border-box; margin: 0; padding: 0; }
  html, body { width: 1200px; height: 1200px; overflow: hidden; }
  body { background: var(--backdrop); position: relative; font-family: var(--sans); color: var(--ink); }

  .sheet { position: absolute; box-shadow: 0 6px 14px rgba(0,0,0,.25); }

  /* Brand name lockup */
  .brand { display: flex; align-items: center; gap: 8px; font-family: var(--serif); font-weight: 500; color: var(--navy); white-space: nowrap; }
  .brand__mark { background: currentColor; flex: none; }

  /* Folder */
  .folder { left: 90px; top: 100px; width: 480px; height: 621px;
    background: linear-gradient(160deg, #2438a8 0%, var(--navy) 45%, var(--navy-deep) 100%); }
  .folder .brand { position: absolute; left: 0; right: 0; top: 280px; justify-content: center; color: #fff; font-size: 34px; gap: 14px; }
  .folder .brand__mark { width: 22px; height: 22px; }
  .folder__web { position: absolute; left: 0; right: 0; bottom: 48px; text-align: center; color: #fff; font-family: var(--serif); font-size: 12px; letter-spacing: .08em; }

  /* Letterhead */
  .letterhead { left: 630px; top: 100px; width: 480px; height: 621px; background: var(--paper); }
  .letterhead__edge { position: absolute; left: 0; top: 0; width: 4px; height: 58px; background: var(--navy); }
  .letterhead .brand { position: absolute; left: 24px; top: 30px; font-size: 15px; }
  .letterhead .brand__mark { width: 10px; height: 10px; }
  .contact-box { position: absolute; right: 24px; top: 24px; width: 170px; padding: 8px 10px; background: var(--navy); color: #fff; text-align: right; font-size: 7.5px; line-height: 1.45; }
  .contact-box__name { font-family: var(--serif); font-size: 8.5px; margin-bottom: 2px; }
  .letter-body { position: absolute; left: 40px; right: 36px; top: 180px; font-size: 7.4px; line-height: 1.75; }
  .letter-body p { margin-bottom: 9px; }
  .signoff { position: absolute; left: 40px; top: 395px; font-size: 7.4px; }
  .signature { display: block; width: 110px; height: 34px; margin: 8px 0 6px; background: linear-gradient(90deg, #e6e7ea, #f4f4f6); }
  .letter-faint { position: absolute; left: 0; right: 0; top: 500px; text-align: center; font-family: var(--serif); font-weight: 500; font-size: 36px; color: var(--faint); }
  .address-band { position: absolute; left: 0; right: 0; bottom: 0; height: 30px; background: var(--navy); color: #fff; display: flex; align-items: center; justify-content: center; font-family: var(--serif); font-size: 9.5px; letter-spacing: .03em; }

  /* Envelope back */
  .envelope-back { left: 90px; top: 900px; width: 480px; height: 208px; background: var(--paper-shade); overflow: hidden; }
  .envelope-back svg { position: absolute; inset: 0; }
  .envelope-back .brand { position: absolute; left: 0; right: 0; top: 42px; justify-content: center; font-size: 16px; }
  .envelope-back .brand__mark { width: 10px; height: 10px; }

  /* Envelope front */
  .envelope-front { left: 630px; top: 900px; width: 480px; height: 208px; background: linear-gradient(180deg, #fff 40%, #e4e6e9 100%); }
  .envelope-front__edge { position: absolute; left: 0; top: 12px; width: 3px; height: 36px; background: var(--navy); }
  .envelope-front .brand { position: absolute; left: 16px; top: 24px; font-size: 11px; gap: 6px; }
  .envelope-front .brand__mark { width: 8px; height: 8px; }
  .envelope-front .contact-box { right: 20px; top: 12px; width: 126px; padding: 5px 7px; font-size: 5.6px; }
  .envelope-front .contact-box__name { font-size: 6.2px; }
  .envelope-front .address-band { height: 20px; font-size: 6.5px; }
</style>
</head>
<body>

<section class="sheet folder">
  <div class="brand"><span class="brand__mark"></span>Tallow &amp; Mersey</div>
  <div class="folder__web">WWW.TALLOWANDMERSEY.EXAMPLE</div>
</section>

<section class="sheet letterhead">
  <div class="letterhead__edge"></div>
  <div class="brand"><span class="brand__mark"></span>Tallow &amp; Mersey</div>
  <div class="contact-box">
    <div class="contact-box__name">TALLOW &amp; MERSEY, LLP</div>
    (555) 408-1936 &#9742;<br>(555) 408-2275 &#9670;<br>www.tallowandmersey.example
  </div>
  <div class="letter-body">
    <p>Lorem ipsum dolor sit amet, consectetur adipiscing elit. Donec eget nisi eget tortor iaculis tristique. Aliquam tincidunt posuere tortor hendrerit elementum. Nunc laoreet lorem a sem auctor fringilla. Pellentesque dignissim accumsan lobortis. Sed pharetra erat vitae dui imperdiet quis commodo orci dapibus. Cum sociis natoque penatibus et magnis dis parturient montes, nascetur ridiculus mus. Fusce at nunc libero. Nam metus lorem, rhoncus ac mattis ornare, blandit vel risus.</p>
    <p>Vestibulum ante ipsum primis in faucibus orci luctus et ultrices posuere cubilia Curae; Ut sit amet augue eget purus facilisis suscipit. Sed vitae risus nibh. Vivamus at sollicitudin ipsum. Vestibulum consectetur dictum egestas. Nam eu tortor non mauris condimentum rutrum eu at urna. Vivamus quis odio et velit aliquet adipiscing quis quis diam. Quisque facilisis molestie neque, in consequat tortor viverra eu.</p>
    <p>Etiam tincidunt aliquam porta. Phasellus ut nisi nibh. Pellentesque non nulla nisi. Sed interdum porta leo ut interdum. Integer molestie, libero quis pellentesque gravida, sapien sem varius est, vel sagittis libero sapien id nulla. Vivamus aliquam nulla vitae mi sodales sit amet semper nulla pulvinar. Nulla congue sagittis auctor. Pellentesque sollicitudin mollis libero.</p>
  </div>
  <div class="signoff">
    Yours faithfully,
    <span class="signature" role="img" aria-label="Handwritten signature"></span>
    Jordan Avery Hale
  </div>
  <div class="letter-faint">Tallow &amp; Mersey</div>
  <div class="address-band">7183 CORVID LANE, SUITE 1000, BRENFORD, TX 75591</div>
</section>

<section class="sheet envelope-back">
  <svg width="480" height="208" viewBox="0 0 480 208">
    <rect x="0" y="0" width="480" height="208" fill="#eceef0"/>
    <path d="M0 208 L175 92 L305 92 L480 208 Z" fill="#e2e4e7"/>
    <path d="M0 14 L0 30 L200 110 Q240 124 280 110 L480 30 L480 14 Z" fill="#f7f7f8" stroke="#d3d6da" stroke-width="1"/>
    <rect x="0" y="0" width="480" height="14" fill="#1d2f96"/>
  </svg>
  <div class="brand"><span class="brand__mark"></span>Tallow &amp; Mersey</div>
</section>

<section class="sheet envelope-front">
  <div class="envelope-front__edge"></div>
  <div class="brand"><span class="brand__mark"></span>Tallow &amp; Mersey</div>
  <div class="contact-box">
    <div class="contact-box__name">TALLOW &amp; MERSEY, LLP</div>
    (555) 408-1936 &#9742;<br>(555) 408-2275 &#9670;<br>www.tallowandmersey.example
  </div>
  <div class="address-band">7183 CORVID LANE, SUITE 1000, BRENFORD, TX 75591</div>
</section>

</body>
</html>
```